Harlow Ridge Partners Business Cards

Design Business cards in a format where I can change the information and utilize a third party buisness card printing company

Contact Information for Business Card

Want Logo and Name on Back. Looking for Spot UV style shine on Logo. Probably Black background. Want smaller logo on front with contact details. Like rounded edges or something else interesting.

Requirements
Must have
• Strong masculine look.

```html
<!DOCTYPE html>
<html lang="en">
<head>
<meta charset="utf-8">
<title>Harlow Ridge Partners – Business Cards</title>
<link rel="stylesheet" href="https://fonts.googleapis.com/css2?family=Cinzel:wght@400;600&display=swap">
<style>
  :root {
    --backdrop: #1b1b1c;
    --card-top: #1c1c1d;
    --card-bottom: #0e0e0f;
    --ink-silver: #8c8c8e;
    --ink-white: #f2f2f2;
    --ink-muted: #7a7a7c;
  }
  * { box-sizing: border-box; margin: 0; padding: 0; }
  html, body {
    width: 1200px; height: 900px; overflow: hidden;
    background: var(--backdrop);
    font-family: "Cinzel", "Times New Roman", serif;
  }
  .sheet {
    position: relative; width: 1200px; height: 900px;
    display: flex; flex-direction: column; align-items: center; justify-content: center; gap: 48px;
  }
  .card {
    position: relative; width: 660px; height: 377px;
    border-radius: 14px;
    background: linear-gradient(160deg, var(--card-top), var(--card-bottom));
    box-shadow: 0 0 0 1px #2a2a2b;
    overflow: hidden;
  }
  /* Logo side */
  .brand {
    position: absolute; inset: 0;
    display: flex; flex-direction: column; align-items: center; justify-content: center;
    color: var(--ink-silver); font-weight: 600; text-transform: uppercase;
  }
  .brand__name { font-size: 44px; letter-spacing: 2px; line-height: 1; }
  .brand__sub { font-size: 15px; letter-spacing: 14px; margin-top: 8px; padding-left: 14px; }
  /* Contact side */
  .person {
    position: absolute; left: 30px; top: 138px; width: 260px; text-align: right;
  }
  .person__name { font-size: 30px; color: var(--ink-silver); letter-spacing: 1.5px; line-height: 1.1; white-space: nowrap; }
  .person__title { font-size: 16px; color: var(--ink-white); letter-spacing: 1px; margin-top: 2px; }
  .divider {
    position: absolute; left: 312px; top: 140px; width: 2px; height: 64px; background: var(--ink-white);
  }
  .contacts {
    position: absolute; left: 334px; top: 144px; list-style: none;
    font-size: 13.5px; color: var(--ink-white); letter-spacing: 0.3px;
  }
  .contacts li { display: flex; align-items: center; gap: 10px; height: 21px; white-space: nowrap; }
  .contacts svg { width: 12px; height: 12px; flex: none; stroke: var(--ink-muted); fill: none; stroke-width: 1.4; }
  .address {
    position: absolute; left: 60px; bottom: 56px;
    font-size: 17px; color: var(--ink-white); letter-spacing: 0.8px;
  }
</style>
</head>
<body>
<main class="sheet">
  <section class="card card--logo">
    <div class="brand">
      <span class="brand__name">Harlow Ridge</span>
      <span class="brand__sub">Partners</span>
    </div>
  </section>

  <section class="card card--contact">
    <div class="person">
      <p class="person__name">Daniel Carver</p>
      <p class="person__title">Director</p>
    </div>
    <div class="divider"></div>
    <ul class="contacts">
      <li>
        <svg viewBox="0 0 12 12"><path d="M3 1 L5 3.5 L4 5 Q5 7 7 8 L8.5 7 L11 9 L9.5 11 Q4 10.5 1 3 Z"/></svg>
        +330 2471-5163
      </li>
      <li>
        <svg viewBox="0 0 12 12"><rect x="1" y="2.5" width="10" height="7"/><path d="M1 2.5 L6 6.5 L11 2.5"/></svg>
        info@harlowridgepartners.com
      </li>
      <li>
        <svg viewBox="0 0 12 12"><circle cx="6" cy="6" r="5"/><ellipse cx="6" cy="6" rx="2.2" ry="5"/><path d="M1 6 H11"/></svg>
        www.harlowridgepartners.com
      </li>
    </ul>
    <p class="address">12345 Address Street City State Postcode Country</p>
  </section>
</main>
</body>
</html>
```